Wine bottle label for family vineyard

Label front and back for our background vineyard. BeLow is a label we used in the past. The gazebo is at the top of the vineyard. We want the front label to have the info we have currently with name etc. But we are open to fun on the back. Maybe a Covid mask would be appropriate Would like one with and one without. But I want the designer to feel free and go out of the box. Especially on back label.

Target Market(s)

None. It’s just for personal consumption We drink what we can and give the rest away.

Industry/Entity Type

Wine

Requirements
Must have
• Name the quiet glass. Tosbeck family vineyard. Pinot noir. Year. Name of winemaker.
Nice to have
• The back label being fun is a plus. Maybe some quotes about wine and friends

```html
<!DOCTYPE html>
<html lang="en">
<head>
<meta charset="utf-8">
<title>The Quiet Glass – Pinot Noir Labels</title>
<link rel="stylesheet" href="https://fonts.googleapis.com/css2?family=Cinzel:wght@500;600&family=Montserrat:wght@400&family=Oswald:wght@600&family=Poppins:wght@400;500;600&display=swap">
<style>
  :root {
    --backdrop: #d9ccb5;
    --label-cream: #fbf5e8;
    --ink: #1e1b18;
    --ink-soft: #2b2724;
    --band-red: #e01b24;
    --band-text: #ffffff;
    --photo-dark: #8d8b87;
    --photo-mid: #b9b6b0;
    --sketch-brown: #8a5a52;
    --sketch-light: #d9c3b5;
  }
  * { margin: 0; padding: 0; box-sizing: border-box; }
  html, body {
    width: 677px;
    height: 1200px;
    overflow: hidden;
    background: var(--backdrop);
  }
  .label-set {
    position: relative;
    width: 677px;
    height: 1200px;
    display: flex;
    justify-content: center;
    align-items: center;
    gap: 26px;
  }
  .label {
    position: relative;
    width: 300px;
    height: 424px;
    background: var(--label-cream);
    box-shadow: 0 6px 14px rgba(60, 40, 20, 0.25);
    overflow: hidden;
  }

  /* Front label */
  .front-photo {
    position: absolute;
    left: 0; top: 0;
    width: 100%;
    height: 290px;
    background:
      linear-gradient(to bottom, rgba(251,245,232,0) 55%, var(--label-cream) 100%),
      radial-gradient(ellipse at 50% 55%, var(--photo-dark) 0%, var(--photo-mid) 60%, #d6d3cd 100%);
  }
  .front-title {
    position: absolute;
    top: 288px;
    width: 100%;
    text-align: center;
    font-family: "Cinzel", serif;
    font-weight: 600;
    font-size: 28px;
    line-height: 1;
    color: var(--ink);
    letter-spacing: 0.5px;
  }
  .front-title .small-cap { font-size: 22px; }
  .front-vineyard {
    position: absolute;
    top: 319px;
    width: 100%;
    text-align: center;
    font-family: "Montserrat", sans-serif;
    font-size: 9.5px;
    letter-spacing: 3.4px;
    text-transform: uppercase;
    color: var(--ink-soft);
  }
  .front-varietal {
    position: absolute;
    top: 332px;
    width: 100%;
    text-align: center;
    font-family: "Oswald", sans-serif;
    font-weight: 600;
    font-size: 23px;
    letter-spacing: 0.5px;
    color: var(--ink);
  }
  .front-band {
    position: absolute;
    left: 0; bottom: 0;
    width: 100%;
    height: 37px;
    background: var(--band-red);
    display: flex;
    align-items: center;
    justify-content: center;
    font-family: "Poppins", sans-serif;
    font-weight: 600;
    font-size: 10.5px;
    color: var(--band-text);
  }
  .front-band .divider { margin: 0 4px; font-weight: 400; }

  /* Back label */
  .back-quote {
    position: absolute;
    top: 62px;
    width: 100%;
    text-align: center;
    font-family: "Poppins", sans-serif;
    font-weight: 500;
    font-size: 18px;
    line-height: 29.5px;
    color: var(--ink);
  }
  .back-credit {
    position: absolute;
    top: 213px;
    width: 100%;
    text-align: center;
    font-family: "Poppins", sans-serif;
    font-weight: 400;
    font-size: 11.5px;
    line-height: 17px;
    color: var(--ink);
  }
  .back-landscape {
    position: absolute;
    left: 0; bottom: 0;
    width: 100%;
    height: 127px;
    background:
      linear-gradient(to bottom, var(--label-cream) 0%, var(--sketch-light) 35%, #c29f92 60%, var(--sketch-brown) 100%);
    opacity: 0.75;
  }
</style>
</head>
<body>
  <main class="label-set">
    <section class="label label-front">
      <div class="front-photo" role="img" aria-label="Black and white photograph of a wooden garden gazebo among trees at the top of the vineyard"></div>
      <h1 class="front-title">T<span class="small-cap">HE</span> Q<span class="small-cap">UIET</span> G<span class="small-cap">LASS</span></h1>
      <p class="front-vineyard">A Tosbeck Family Vineyard</p>
      <p class="front-varietal">PINOT NOIR</p>
      <div class="front-band">
        Sonoma Border<span class="divider">|</span>Novato<span class="divider">|</span>Marin County 2016
      </div>
    </section>

    <section class="label label-back">
      <blockquote class="back-quote">
        I Love Everything<br>
        That Is Old,<br>
        Old Friends, Old Times,<br>
        Old Manners,<br>
        Old Book, Old Wines
      </blockquote>
      <p class="back-credit">Edmund Farrow,<br>The Parson of Ashfield</p>
      <div class="back-landscape" role="img" aria-label="Brown ink sketch of mountains above rolling vineyard rows with cypress trees and farmhouses"></div>
    </section>
  </main>
</body>
</html>
```